Voice agent website redesign, responsive. Current website functional, needs fresh look.

** updated 01/04/2015 ** Stock photos and video OK
TQ Sounds is redesigning their website to refresh the look and feel and also to make the website more useable in portable devices.
We also intend to replace our existing iPhone app with responsive HTML.
We want to keep the features but update the way they are displayed.
The current website is at: http://www.tqsounds-demo.com.au. (examples of important pages are in the attachments)
The current website is written in .NET and MS SQL but designs optimised for WordPress will also be accepted.
We have corporate colours and a logo
We want a dynamic element on the front page
We do not mind the idea of a slider, but I must be modern and capable of video backgrounds
We like the clean design of our main competitor: http://www.zelvar-demo.com.au but the site is busy and not responsive.
The site must be designed to use responsive HTML and be easy to see and navigate using smaller viewports.
Once awarded the contract the designer must supply 4 pages in 3 formats, for which we will pay an extra $80, as outlined below:
Submission for selection
Designs must be submitted for selection with 1 required page (home page) in 1 required resolution and 1 optional resolution;
Versions:
• (Required) Full page web landscape – 1920 x 1080
• (Optional) Low resolution portrait (e.g. iPhone 3/4) – 320 x 480
Submission required when awarded
Final supplied designs must have 3 versions of 4 required pages as layered Photoshop files;
Versions:
• Full page web landscape – 1920 x 1080
• Medium resolution landscape (e.g. iPad) – 1024 x 768
• Low resolution portrait (e.g. iPhone 3/4) – 320 x 480
Pages:
• home page
• generic template
• search results
• talent page
The designer may also offer to convert the site into HTML and CSS for an added fee.
The attachments supplied contains important features like site menu and required elements, but only guidelines to design.
Please do read carefully for details on required elements, but do feel free to change the design, look and feel completely.
Attached are;
Target Market(s)
Advertising agencies who hire voice artists, also a showcase for the artists themselves
Look and feel

```html
<!DOCTYPE html>
<html lang="en">
<head>
<meta charset="utf-8">
<title>TQ Sounds – Home</title>
<link href="https://fonts.googleapis.com/css2?family=Hind:wght@400;500;600&family=Sansita:wght@700&family=Lato:ital@1&display=swap" rel="stylesheet">
<style>
:root{
  --green:#8dc63f;
  --green-dark:#6aa12a;
  --navy:#143a5c;
  --navy-deep:#0f3150;
  --sky:#c9dde9;
  --white:#ffffff;
  --ink:#1d3550;
  --wood:#a5682c;
  --wood-dark:#7a4718;
  --paper:#e4efd7;
  --input:#4f7fa0;
}
*{box-sizing:border-box;margin:0;padding:0}
html,body{width:1200px;height:675px;overflow:hidden}
body{position:relative;font-family:"Hind",sans-serif;color:var(--white);
  background:linear-gradient(180deg,var(--navy-deep) 0%,#1c4d74 25%,#4f84aa 55%,#9cc0d7 80%,var(--sky) 95%);}
.abs{position:absolute}
.header-band{left:0;top:0;width:1200px;height:86px;background:linear-gradient(180deg,#0d2e4c,#123c5f);box-shadow:0 3px 8px rgba(0,0,0,.35)}
.brand{left:232px;top:18px;display:flex;align-items:center;gap:8px}
.brand-name{font-size:24px;font-weight:600;color:var(--white);line-height:1}
.brand-dot{width:18px;height:18px;border-radius:50%;background:var(--green)}
.phone{left:600px;top:12px;font-size:12.5px;color:var(--green);display:flex;align-items:center;gap:6px}
.header-rule{left:405px;top:40px;width:555px;height:1px;background:rgba(141,198,63,.6)}
.nav{left:403px;top:41px;display:flex;height:43px}
.nav a{display:flex;align-items:center;padding:0 7px;font-size:12px;font-weight:500;color:var(--green);text-decoration:none}
.nav a.active{background:var(--white);color:var(--ink);border-bottom:4px solid var(--green)}
.social{display:flex;gap:5px}
.social span{width:17px;height:17px;border-radius:50%;background:#9aa8b4;display:block}
.social span.first{background:var(--green)}
.header-social{left:821px;top:53px}
.section-title{font-family:"Sansita",sans-serif;font-weight:700}
.recent{left:488px;top:93px;width:480px;text-align:center;font-size:16px}
.recent-rule{left:675px;top:115px}
.board-string{left:240px;top:95px}
.board{left:240px;top:148px;width:230px;height:260px;border-radius:6px;
  background:linear-gradient(90deg,var(--wood-dark),var(--wood) 20%,#b97a3a 50%,var(--wood) 80%,var(--wood-dark));
  box-shadow:0 4px 8px rgba(0,0,0,.45)}
.board-paper{position:absolute;left:10px;top:9px;width:210px;height:240px;background:linear-gradient(180deg,#eef5e6,var(--paper));border-radius:2px}
.board-title{position:absolute;left:0;top:14px;width:100%;text-align:center;font-size:15px;color:var(--navy)}
.select{position:absolute;height:24px;background:var(--white);border:1px solid #b9c4cc;border-radius:3px;
  box-shadow:0 2px 3px rgba(0,0,0,.25);font-family:"Lato",sans-serif;font-style:italic;font-size:10.5px;color:var(--ink);
  display:flex;align-items:center;justify-content:space-between;padding:0 7px}
.select::after{content:"";border:4px solid transparent;border-top:5px solid var(--ink);margin-top:4px}
.btn{position:absolute;height:23px;background:var(--white);border:1px solid #8fa0ae;border-radius:3px;box-shadow:0 2px 3px rgba(0,0,0,.3);
  font-family:"Lato",sans-serif;font-style:italic;font-size:10.5px;color:var(--ink);display:flex;align-items:center;justify-content:center}
.video-frame{left:488px;top:132px;width:480px;height:281px;background:#2b2b2b;border:3px solid #444;box-shadow:0 3px 10px rgba(0,0,0,.5)}
.video-still{position:absolute;left:4px;top:4px;right:4px;bottom:4px;background:linear-gradient(135deg,#9a9894,#c9c5be 45%,#7c7f84 80%,#5e5e63)}
.play{position:absolute;left:206px;top:111px;width:66px;height:46px;border-radius:8px;background:var(--green);opacity:.9;display:flex;align-items:center;justify-content:center}
.tab{height:42px;background:var(--white);box-shadow:0 3px 4px rgba(0,0,0,.3);border-bottom:3px solid var(--green);
  display:flex;align-items:center;gap:6px;padding:0 8px;font-size:15px;color:var(--navy)}
.tab-news{left:363px;top:430px;width:122px}
.tab-spot{left:722px;top:430px;width:124px}
.avatar{width:72px;height:72px;border-radius:50%;border:6px solid var(--green);background:radial-gradient(circle,#bdbdbd,#6d6d6d)}
.news-avatar{left:230px;top:494px}
.spot-avatar{left:601px;top:494px}
.copy{font-size:9.3px;line-height:12.6px}
.news-copy{left:310px;top:491px;width:283px;text-align:justify;color:var(--white)}
.news-copy a{color:var(--ink);text-decoration:none}
.spot-copy{left:681px;top:513px;width:280px;text-align:justify;color:var(--ink)}
.spot-copy b{font-weight:500;color:#000}
.spot-meta{left:866px;top:558px;font-size:9.5px;line-height:12.6px;color:var(--ink)}
.newsletter-label{left:370px;top:604px;font-size:9.5px;color:var(--ink)}
.newsletter-input{left:527px;top:601px;width:252px;height:21px;background:var(--input);border-radius:2px;
  font-family:"Lato",sans-serif;font-style:italic;font-size:10px;color:#dce8f0;padding:4px 12px}
.subscribe{left:781px;top:601px;width:48px;height:21px;background:var(--green);border:1px solid #fff;font-size:8.5px;font-weight:600;color:var(--white);display:flex;align-items:center;justify-content:center}
.footer{left:0;top:647px;width:1200px;height:28px;background:var(--green);color:var(--white);font-size:9.5px}
.footer .copyright{position:absolute;left:234px;top:9px}
.footer .copyright span{color:var(--ink)}
.footer-social{position:absolute;left:532px;top:5px}
.footer-social span{background:var(--white)}
.footer .legal{position:absolute;left:711px;top:9px}
</style>
</head>
<body>
<div class="abs header-band"></div>
<div class="abs brand"><span class="brand-dot"></span><span class="brand-name">TQ Sounds</span></div>
<div class="abs phone">
  <svg width="13" height="13" viewBox="0 0 16 16"><rect width="16" height="16" rx="3" fill="#8dc63f"/><path d="M5 3.5l2 2-1 1.3c.6 1.3 1.6 2.3 2.9 2.9l1.3-1 2 2-1.2 1.6C7.5 12 4 8.5 3.6 4.7z" fill="#0f3150"/></svg>
  Call Now From Sydney &nbsp;+ 61200000000 &nbsp;and Melbourne &nbsp;+ 61300000000...
</div>
<div class="abs header-rule"></div>
<nav class="abs nav">
  <a class="active" href="#">Home</a><a href="#">Rates</a><a href="#">About Us</a><a href="#">FAQs</a><a href="#">Payments</a><a href="#">Login</a><a href="#">Contact</a>
</nav>
<div class="abs social header-social" aria-label="Social links"><span class="first"></span><span></span><span></span><span></span><span></span><span></span></div>

<div class="abs section-title recent">Recent Works</div>
<svg class="abs recent-rule" width="112" height="16" viewBox="0 0 112 16"><line x1="0" y1="8" x2="40" y2="8" stroke="#8dc63f"/><line x1="72" y1="8" x2="112" y2="8" stroke="#8dc63f"/><rect x="53" y="2" width="6" height="11" rx="3" fill="#8dc63f"/><path d="M48 4a9 9 0 0 0 0 8M64 4a9 9 0 0 1 0 8" stroke="#8dc63f" fill="none"/></svg>

<svg class="abs board-string" width="230" height="70" viewBox="0 0 230 70"><path d="M16 64L115 10L214 64" stroke="#2b2b2b" stroke-width="1.5" fill="none"/><circle cx="115" cy="10" r="7" fill="#cfd6dc" stroke="#555"/><circle cx="115" cy="10" r="3" fill="#555"/></svg>
<div class="abs board">
  <div class="board-paper">
    <div class="board-title section-title">Our Artists</div>
    <div class="select" style="left:46px;top:36px;width:126px">Search By Name</div>
    <div class="select" style="left:6px;top:73px;width:94px">Location</div>
    <div class="select" style="left:111px;top:73px;width:95px">Sex</div>
    <div class="select" style="left:6px;top:110px;width:94px">Voice Type</div>
    <div class="select" style="left:111px;top:110px;width:95px">Age</div>
    <div class="select" style="left:6px;top:148px;width:94px">Language</div>
    <div class="select" style="left:111px;top:148px;width:95px">Accent</div>
    <div class="btn" style="left:22px;top:193px;width:80px">See All Artists</div>
    <div class="btn" style="left:109px;top:193px;width:80px">Find &nbsp;&nbsp;&nbsp;&#9656;</div>
  </div>
</div>

<div class="abs video-frame">
  <div class="video-still" role="img" aria-label="Video still from a recent advertisement: two young men on a sofa in a living room"></div>
  <div class="play"><svg width="24" height="24" viewBox="0 0 24 24"><path d="M5 2l17 10L5 22z" fill="#1d3550" opacity=".8"/></svg></div>
</div>

<div class="abs tab tab-news section-title"><svg width="14" height="26" viewBox="0 0 14 26"><rect x="3" y="0" width="8" height="15" rx="3" fill="#8dc63f"/><path d="M1 10a6 6 0 0 0 12 0M7 16v6M2 24h10" stroke="#8dc63f" stroke-width="2" fill="none"/></svg>Latest News</div>
<div class="abs tab tab-spot section-title"><svg width="14" height="26" viewBox="0 0 14 26"><rect x="3" y="0" width="8" height="15" rx="3" fill="#8dc63f"/><path d="M1 10a6 6 0 0 0 12 0M7 16v6M2 24h10" stroke="#8dc63f" stroke-width="2" fill="none"/></svg>Spot Light</div>

<div class="abs avatar news-avatar" role="img" aria-label="Portrait photo of featured voice artist"></div>
<p class="abs copy news-copy">A big warm welcome to Mara Lindqvist, a rising star of the voice over world. She's been the girl next door, a cut glass Brit, a mum, your date, your mate in a wide variety of campaigns, and she takes particular pleasure in a deep, honey-throated soft sell. You probably knew her as head nurse on Harbour Ward for many years, and she now plays a high-flying lawyer on Close Calls. Check out her <a href="#">demo</a> here.</p>

<div class="abs avatar spot-avatar" role="img" aria-label="Portrait photo of spotlight actor"></div>
<p class="abs copy spot-copy">Owen Hartley has been a screen and theatre actor for over twenty years. He has many film credits to his name, most recently as director of the acclaimed feature film "The Long Road". <b>See More...</b></p>
<p class="abs spot-meta">Name : Loriem ipsum,<br>Place : &nbsp;Us.</p>

<div class="abs newsletter-label">We are Keep In Touch via News Letter</div>
<div class="abs newsletter-input">Email</div>
<div class="abs subscribe">Subscribe</div>

<footer class="abs footer">
  <div class="copyright">© Copyright 2015 <span>TQ Sounds Pvt Limited.</span></div>
  <div class="social footer-social" aria-label="Social links"><span></span><span></span><span></span><span></span><span></span><span></span></div>
  <div class="legal">Privacy Policy &amp; Terms and Conditions &nbsp;&nbsp;&nbsp;|&nbsp;&nbsp;&nbsp; Website by &nbsp;Kestrel Web.</div>
</footer>
</body>
</html>
```